New business card for civil engineering company - "Keystone Audit"

We need a business card designed for our new structural engineering company.

The company name is "Keystone Audit" logo files attached.

We would like the following:
* Two-sided card
* Simple design

Information to be placed on the card:
Name - Marcus Dellow
Job Title - Director / Structural Engineer
Credentials - BEng(Hons), CPEng, CMengNZ, IntPE(NZ)
Email - marcus.dellow@keystoneaudit.co.nz
mobile - 0219364058
website - www.keystoneaudit.co.nz

```html
<!DOCTYPE html>
<html lang="en">
<head>
<meta charset="utf-8">
<title>Keystone Audit – Business Card</title>
<link rel="stylesheet" href="https://fonts.googleapis.com/css2?family=Montserrat:wght@400;500;700&display=swap">
<style>
  :root {
    --backdrop: #3a302b;
    --card: #2e2f31;
    --edge: #2b9fdc;
    --accent: #2f9be0;
    --text: #f1f1f1;
    --text-muted: #b9bcc0;
    --front-mark: #1b1c1e;
    --divider: #8c8f93;
  }
  * { box-sizing: border-box; margin: 0; padding: 0; }
  html, body {
    width: 1200px;
    height: 800px;
    overflow: hidden;
    background: var(--backdrop);
    font-family: "Montserrat", sans-serif;
  }
  .stage {
    width: 1200px;
    height: 800px;
    display: flex;
    align-items: center;
    justify-content: center;
    gap: 40px;
  }
  .card {
    width: 540px;
    height: 309px;
    background: var(--card);
    border-left: 3px solid var(--edge);
    border-bottom: 3px solid var(--edge);
    position: relative;
    box-shadow: 0 10px 24px rgba(0,0,0,0.35);
  }
  /* Front side */
  .card--front {
    display: flex;
    align-items: center;
    justify-content: center;
  }
  .brand {
    display: flex;
    align-items: center;
    gap: 10px;
  }
  .brand__square {
    width: 14px;
    height: 14px;
    background: var(--accent);
  }
  .brand__name {
    font-weight: 700;
    text-transform: uppercase;
    letter-spacing: 2px;
  }
  .card--front .brand__name {
    font-size: 30px;
    color: var(--front-mark);
  }
  /* Back side */
  .card--back {
    display: flex;
    align-items: center;
    padding: 0 24px 0 30px;
  }
  .card--back .brand {
    width: 200px;
  }
  .card--back .brand__name {
    font-size: 17px;
    color: var(--text);
  }
  .divider {
    width: 1px;
    height: 140px;
    background: var(--divider);
    margin: 0 20px 0 12px;
  }
  .contact__name {
    font-size: 17px;
    font-weight: 700;
    color: var(--accent);
    text-transform: uppercase;
    letter-spacing: 1px;
  }
  .contact__role,
  .contact__credentials {
    font-size: 12px;
    color: var(--text);
    line-height: 1.4;
  }
  .contact__credentials { margin-top: 6px; }
  .contact__list {
    list-style: none;
    margin-top: 8px;
  }
  .contact__item {
    display: flex;
    align-items: center;
    gap: 8px;
    font-size: 12px;
    color: var(--text);
    line-height: 1.55;
  }
  .contact__icon {
    width: 11px;
    height: 11px;
    flex: none;
    fill: var(--accent);
  }
</style>
</head>
<body>
<main class="stage">
  <section class="card card--front" aria-label="Card front">
    <div class="brand">
      <span class="brand__square"></span>
      <span class="brand__name">Keystone Audit</span>
    </div>
  </section>

  <section class="card card--back" aria-label="Card back">
    <div class="brand">
      <span class="brand__square"></span>
      <span class="brand__name">Keystone Audit</span>
    </div>
    <div class="divider"></div>
    <div class="contact">
      <h1 class="contact__name">Marcus Dellow</h1>
      <p class="contact__role">Director / Structural Engineer</p>
      <p class="contact__credentials">Credentials - BEng(Hons)<br>CPEng, CMengNZ, IntPE(NZ)</p>
      <ul class="contact__list">
        <li class="contact__item">
          <svg class="contact__icon" viewBox="0 0 24 24" aria-hidden="true"><path d="M6.6 10.8a15.1 15.1 0 0 0 6.6 6.6l2.2-2.2c.3-.3.7-.4 1-.2 1.1.4 2.3.6 3.6.6.6 0 1 .4 1 1V20c0 .6-.4 1-1 1C10.6 21 3 13.4 3 4c0-.6.4-1 1-1h3.5c.6 0 1 .4 1 1 0 1.3.2 2.5.6 3.6.1.3 0 .7-.2 1z"/></svg>
          <span>0219364058</span>
        </li>
        <li class="contact__item">
          <svg class="contact__icon" viewBox="0 0 24 24" aria-hidden="true"><path d="M2 5h20v14H2z M2 5l10 8 10-8" fill="none" stroke="currentColor"/><path d="M2 5h20v2l-10 7L2 7z M2 9l10 7 10-7v10H2z"/></svg>
          <span>marcus.dellow@keystoneaudit.co.nz</span>
        </li>
        <li class="contact__item">
          <svg class="contact__icon" viewBox="0 0 24 24" aria-hidden="true"><circle cx="12" cy="12" r="10"/></svg>
          <span>www.keystoneaudit.co.nz</span>
        </li>
      </ul>
    </div>
  </section>
</main>
</body>
</html>
```